Bref créative
Business Cards, Letterhead, and Envelope
Cordova Peak Realty Group Inc.
Simple
4236 Fernway Crest Blvd.
South Gate, CA 90280
Morvani@cordovapeak.com
DRE#07246318
Pls feel Free to be creative
Bullet points or any creative design but needs following pointers
- First time buyer Programs
- Multi-Unit property Programs
- Low down payment Programs
- $ 0 Closing costs available

```html
<!DOCTYPE html>
<html lang="en">
<head>
<meta charset="utf-8">
<title>Cordova Peak Realty Group Inc. – Business Card</title>
<link href="https://fonts.googleapis.com/css2?family=Arimo:wght@400;600;700&display=swap" rel="stylesheet">
<style>
  :root {
    --page-bg: #e6e4e1;
    --silver-light: #fbfbfb;
    --silver-mid: #dcdcdc;
    --silver-dark: #b9b9b9;
    --orange-light: #ffb638;
    --orange: #f39a12;
    --orange-deep: #e07f05;
    --ink: #3a3a3a;
    --ink-soft: #5c5c5c;
  }
  * { box-sizing: border-box; margin: 0; padding: 0; }
  html, body { width: 1200px; height: 811px; overflow: hidden; }
  body {
    background: var(--page-bg);
    font-family: "Arimo", Arial, sans-serif;
    color: var(--ink);
    display: flex;
    align-items: center;
    justify-content: center;
    gap: 48px;
  }
  .card {
    position: relative;
    width: 540px;
    height: 309px;
    background: linear-gradient(160deg, var(--silver-light) 0%, var(--silver-mid) 55%, var(--silver-dark) 100%);
    box-shadow: 0 6px 18px rgba(0,0,0,.18);
    overflow: hidden;
  }
  .card__band {
    position: absolute;
    left: 0; bottom: 0;
    width: 100%; height: 130px;
  }
  .brand {
    position: absolute;
    left: 0; right: 0;
    display: flex;
    align-items: center;
    justify-content: center;
    gap: 12px;
  }
  .brand__mark {
    width: 22px; height: 22px;
    background: var(--orange);
  }
  .brand__name {
    font-weight: 700;
    font-size: 27px;
    color: var(--ink);
    letter-spacing: .3px;
  }
  .card--front .brand { top: 72px; }
  .card--back .brand { top: 100px; }
  .agent-name {
    position: absolute;
    top: 122px; left: 0; right: 0;
    text-align: center;
    font-weight: 600;
    font-size: 16px;
    color: var(--ink);
  }
  .contact {
    position: absolute;
    left: 28px; bottom: 18px;
    font-size: 12.5px;
    line-height: 1.5;
    color: var(--ink);
  }
  .contact__address { color: var(--ink-soft); margin-bottom: 4px; }
  .programs {
    position: absolute;
    left: 30px; right: 20px; bottom: 24px;
    list-style: none;
    font-size: 13.5px;
    line-height: 1.65;
    color: #2f2f2f;
    display: grid;
    grid-template-columns: auto auto;
    column-gap: 22px;
    justify-content: start;
  }
  .programs li::before { content: "• "; }
</style>
</head>
<body>

  <section class="card card--front" aria-label="Business card front">
    <svg class="card__band" viewBox="0 0 540 130" preserveAspectRatio="none" aria-hidden="true">
      <defs>
        <linearGradient id="bandFront" x1="0" y1="0" x2="1" y2="1">
          <stop offset="0" stop-color="var(--orange-light)"/>
          <stop offset="0.6" stop-color="var(--orange)"/>
          <stop offset="1" stop-color="var(--orange-deep)"/>
        </linearGradient>
      </defs>
      <path d="M0 70 Q270 20 540 0 L540 130 L0 130 Z" fill="#ffffff" opacity=".85"/>
      <path d="M0 78 Q270 28 540 8 L540 130 L0 130 Z" fill="url(#bandFront)"/>
    </svg>
    <div class="brand">
      <span class="brand__mark"></span>
      <span class="brand__name">Cordova Peak Realty Group Inc.</span>
    </div>
    <p class="agent-name">Adrian T. Morvani</p>
    <div class="contact">
      <p class="contact__address">4236 Fernway Crest Blvd. South Gate, CA 90280</p>
      <p>Cell: 310.555.0148 | Fax: 562.555.0193 | Email: Morvani@cordovapeak.com</p>
      <p>License No.: DRE#07246318</p>
    </div>
  </section>

  <section class="card card--back" aria-label="Business card back">
    <svg class="card__band" viewBox="0 0 540 130" preserveAspectRatio="none" aria-hidden="true">
      <defs>
        <linearGradient id="bandBack" x1="0" y1="0" x2="1" y2="1">
          <stop offset="0" stop-color="var(--orange-light)"/>
          <stop offset="0.6" stop-color="var(--orange)"/>
          <stop offset="1" stop-color="var(--orange-deep)"/>
        </linearGradient>
      </defs>
      <path d="M0 55 Q270 20 540 45 L540 130 L0 130 Z" fill="#ffffff" opacity=".85"/>
      <path d="M0 63 Q270 28 540 53 L540 130 L0 130 Z" fill="url(#bandBack)"/>
    </svg>
    <div class="brand">
      <span class="brand__mark"></span>
      <span class="brand__name">Cordova Peak Realty Group Inc.</span>
    </div>
    <ul class="programs">
      <li>First time buyer Programs</li>
      <li>Multi-Unit property Programs</li>
      <li>Low down payment Programs</li>
      <li>$ 0 Closing costs available</li>
    </ul>
  </section>

</body>
</html>
```